Tarrow Creek plumbing plumbing company business card design

Something sinilar to business card i upload it is my old business card design
And have a good watermark with the logo or majority of the logot in rhe background as watermark

Plumbing business similar to uploaded design with a nice watermark of the logo

Font styles to use
Script

Colors

Designer to choose colors to be used in the design.

```html
<!DOCTYPE html>
<html lang="en">
<head>
<meta charset="utf-8">
<title>Tarrow Creek Plumbing – Business Cards</title>
<link rel="stylesheet" href="https://fonts.googleapis.com/css2?family=Montserrat:wght@400;500;700&display=swap">
<style>
  :root {
    --bg: #e9eaec;
    --card-black: #050505;
    --card-blue: #1479c4;
    --card-blue-deep: #0a66ad;
    --white: #ffffff;
    --accent: #1a86d6;
    --mark-dark: rgba(140, 128, 150, 0.55);
    --mark-light: rgba(255, 255, 255, 0.12);
    --shadow: rgba(0, 0, 0, 0.28);
  }
  * { box-sizing: border-box; margin: 0; padding: 0; }
  html, body {
    width: 1200px;
    height: 1021px;
    overflow: hidden;
    background: var(--bg);
    font-family: "Montserrat", sans-serif;
    color: var(--white);
  }
  .canvas { position: relative; width: 1200px; height: 1021px; }

  .card {
    position: absolute;
    width: 640px;
    height: 366px;
    border-radius: 4px;
    box-shadow: 0 14px 30px var(--shadow);
    overflow: hidden;
  }

  .watermark { position: absolute; border-radius: 60px 24px 24px 60px; }

  /* Front (black) */
  .card--front {
    left: 320px;
    top: 90px;
    background: var(--card-black);
  }
  .card--front .watermark {
    left: 70px;
    top: 40px;
    width: 370px;
    height: 250px;
    background: radial-gradient(ellipse at 35% 10%, var(--mark-dark) 0%, rgba(60, 55, 68, 0.25) 45%, rgba(5, 5, 5, 0) 80%);
  }
  .front-brand {
    position: absolute;
    right: 46px;
    bottom: 82px;
    text-align: right;
  }
  .front-brand .brand-name {
    font-weight: 700;
    font-size: 30px;
    letter-spacing: 0.5px;
    line-height: 1.1;
  }
  .front-web {
    position: absolute;
    right: 46px;
    bottom: 40px;
    font-size: 17px;
    font-weight: 400;
    letter-spacing: 0.4px;
  }
  .front-web .domain { color: var(--accent); }

  /* Back (blue) */
  .card--back {
    left: 220px;
    top: 520px;
    background: linear-gradient(135deg, var(--card-blue) 0%, var(--card-blue-deep) 100%);
  }
  .card--back .watermark {
    left: 330px;
    top: 120px;
    width: 330px;
    height: 270px;
    background: linear-gradient(160deg, var(--mark-light) 0%, rgba(255, 255, 255, 0.05) 100%);
  }
  .back-brand {
    position: absolute;
    left: 40px;
    top: 42px;
    font-weight: 700;
    font-size: 30px;
    letter-spacing: 0.5px;
  }
  .contact-list {
    position: absolute;
    left: 40px;
    bottom: 78px;
    list-style: none;
    font-size: 17px;
    line-height: 26px;
    font-weight: 400;
  }
  .contact-list li { display: flex; align-items: center; gap: 8px; }
  .contact-list svg { width: 15px; height: 15px; flex: none; }
  .licence {
    position: absolute;
    left: 40px;
    bottom: 40px;
    font-size: 17px;
  }
  .person {
    position: absolute;
    right: 48px;
    top: 200px;
    text-align right;
    text-align: right;
  }
  .person-name { font-size: 24px; font-weight: 700; letter-spacing: 0.4px; }
  .person-role { font-size: 18px; font-weight: 400; margin-top: 2px; }
</style>
</head>
<body>
<main class="canvas">

  <section class="card card--front">
    <div class="watermark" role="img" aria-label="Large faint brand mark watermark"></div>
    <div class="front-brand">
      <div class="brand-name">Tarrow Creek Plumbing</div>
    </div>
    <div class="front-web"><span class="domain">tarrowcreekplumbing</span>.com.au</div>
  </section>

  <section class="card card--back">
    <div class="watermark" role="img" aria-label="Large faint brand mark watermark"></div>
    <div class="back-brand">Tarrow Creek Plumbing</div>

    <ul class="contact-list">
      <li>
        <svg viewBox="0 0 16 16" aria-hidden="true"><path fill="#fff" d="M3.6 1.2l2.3 2.6-1.3 1.8c.8 1.9 2.3 3.4 4.2 4.3l1.8-1.3 2.6 2.3-1.2 2.3C6.9 13.4 2.6 9.1 1.4 3.5z"/></svg>
        0400 555 219
      </li>
      <li>
        <svg viewBox="0 0 16 16" aria-hidden="true"><rect x="1.5" y="3.5" width="13" height="9" fill="none" stroke="#fff" stroke-width="1.4"/><path d="M1.5 3.5l6.5 5 6.5-5" fill="none" stroke="#fff" stroke-width="1.4"/></svg>
        info@tarrowcreekplumbing.com.au
      </li>
      <li>
        <svg viewBox="0 0 16 16" aria-hidden="true"><g fill="none" stroke="#fff" stroke-width="1.2"><circle cx="8" cy="8" r="6.3"/><ellipse cx="8" cy="8" rx="2.8" ry="6.3"/><path d="M1.7 8h12.6M2.6 4.8h10.8M2.6 11.2h10.8"/></g></svg>
        tarrowcreekplumbing.com.au
      </li>
    </ul>
    <div class="licence">Lic No. 480731c</div>

    <div class="person">
      <div class="person-name">Dean Holloway</div>
      <div class="person-role">Director</div>
    </div>
  </section>

</main>
</body>
</html>
```